Core Values - Poster

Develop a poster to display core values int he company. The design has to be align to the character and feel of the company. See our website for some inspiration. The Core Values are also listed on our website.
Our 4 core values are:
Excellence
We deliver quality services of unmatched value, constantly raising the bar on our performance, through a commitment to excellence, innovation, teamwork, ongoing learning, continuous improvement, an intense focus on client needs, and a dedication to meet those needs with a sense of urgency.
Integrity
We demonstrate honesty, fairness, openness and clear boundaries in all our interactions, behaviours and practices within the organisation and with our clients, stakeholders and the wider community. We act in accordance with our values, even when it’s difficult. We adhere to the highest ethical standards as we strive to do what is right and fair for our clients and for each other.
Sincerity
We embrace human emotions and values, and believe that sincerity is a fundamental human behaviour. We are honest with our team, and with clients in the work we do, and the way we do it. We set high expectations for ourselves to motivate hard work, and we will offer clients something that has been crafted with care, consideration and with authenticity, without cutting corners. We will put people first, and will always genuinely care.
Humility
We believe in a flat hierarchy, and that every person within the organisation is a floor sweeper. We’re not always right — we don’t have all the answers — and we know it. We’re all humans after all, and we’re not afraid to ask for help. We encourage everyone to Be Yourself, Be Open, Stay Hungry and Humble, Collaborate, Challenge, Decide and Just Do.
Everything in our Core Values need to be on the poster, which will be large (minimum 4x A4 size).
Our logo is attached in this brief - there are several colour options and layouts. Logo should be include in the poster.

```html
<!DOCTYPE html>
<html lang="en">
<head>
<meta charset="utf-8">
<title>Core Values Poster</title>
<link href="https://fonts.googleapis.com/css2?family=Montserrat:wght@600;700&family=Open+Sans:wght@400;600&display=swap" rel="stylesheet">
<style>
  :root {
    --forest: #34331f;
    --leaf: #6e9a34;
    --leaf-dark: #5a7f29;
    --paper: #ffffff;
    --card: #f7f6f0;
    --ink: #3a3926;
    --line: #d9d6c4;
  }
  * { box-sizing: border-box; margin: 0; padding: 0; }
  html, body { width: 849px; height: 1200px; overflow: hidden; }
  body {
    position: relative;
    background: var(--forest);
    font-family: "Open Sans", Arial, sans-serif;
    color: var(--ink);
  }
  .brand-area {
    position: absolute; left: 0; top: 0;
    width: 470px; height: 170px;
    background: var(--paper);
    border-bottom-right-radius: 40px;
  }
  .brand {
    position: absolute; left: 30px; top: 40px;
    display: flex; align-items: center; gap: 16px;
  }
  .brand-dot {
    width: 58px; height: 58px; border-radius: 50%;
    background: var(--leaf);
  }
  .brand-name {
    font-family: "Montserrat", Arial, sans-serif;
    font-weight: 600; font-size: 38px; line-height: 1.05;
    color: var(--forest);
  }
  .title-card {
    position: absolute; left: 250px; top: 175px;
    width: 350px; height: 250px;
    background: var(--paper);
    border-radius: 175px 175px 0 0 / 110px 110px 0 0;
    display: flex; align-items: center; justify-content: center;
    padding-top: 40px;
  }
  .title-card h1 {
    font-family: "Montserrat", Arial, sans-serif;
    font-weight: 700; font-size: 58px; line-height: 1.05;
    text-align: center; color: var(--forest);
  }
  .value {
    position: absolute; bottom: 12px;
    background: var(--card);
    border: 2px solid var(--line);
    border-radius: 100px 100px 0 0 / 70px 70px 0 0;
    padding: 30px 14px 0;
    text-align: center;
  }
  .value-icon {
    width: 80px; height: 80px; margin: 0 auto 16px;
    border-radius: 50%; background: var(--leaf);
    display: flex; align-items: center; justify-content: center;
  }
  .value-icon svg { width: 46px; height: 46px; }
  .value h2 {
    font-family: "Montserrat", Arial, sans-serif;
    font-weight: 700; font-size: 27px;
    color: var(--leaf-dark); margin-bottom: 10px;
  }
  .value p { font-size: 12.6px; line-height: 1.42; }
  .sincerity  { left: 14px;  width: 206px; top: 395px; }
  .excellence { left: 222px; width: 202px; top: 465px; }
  .humility   { left: 426px; width: 202px; top: 495px; }
  .integrity  { left: 630px; width: 206px; top: 355px; }
</style>
</head>
<body>
  <div class="brand-area">
    <div class="brand">
      <span class="brand-dot"></span>
      <span class="brand-name">The Kindred<br>Practice</span>
    </div>
  </div>

  <div class="title-card"><h1>Core<br>Values</h1></div>

  <section class="value sincerity">
    <div class="value-icon">
      <svg viewBox="0 0 24 24" fill="#fff"><path d="M12 21s-7.5-4.6-9.5-9.3C1.2 8.5 3.3 5 6.7 5c2.1 0 3.5 1.2 5.3 3 1.8-1.8 3.2-3 5.3-3 3.4 0 5.5 3.5 4.2 6.7C19.5 16.4 12 21 12 21z"/></svg>
    </div>
    <h2>Sincerity</h2>
    <p>We embrace human emotions and values, and believe that sincerity is a fundamental human behaviour. We are honest with our team, and with clients in the work we do, and the way we do it. We set high expectations for ourselves to motivate hard work, and we will offer clients something that has been crafted with care, consideration and with authenticity, without cutting corners. We will put people first, and will always genuinely care.</p>
  </section>

  <section class="value excellence">
    <div class="value-icon">
      <svg viewBox="0 0 24 24" fill="none" stroke="#fff" stroke-width="1.8"><circle cx="12" cy="9" r="6"/><path d="M8.5 14l-2 8 5.5-3 5.5 3-2-8"/><path d="M12 6.2l.9 1.8 2 .3-1.4 1.4.3 2-1.8-.9-1.8.9.3-2L9.1 8.3l2-.3z" fill="#fff" stroke="none"/></svg>
    </div>
    <h2>Excellence</h2>
    <p>We deliver quality services of unmatched value, constantly raising the bar on our performance, through a commitment to excellence, innovation, teamwork, ongoing learning, continuous improvement, an intense focus on client needs, and a dedication to meet those needs with a sense of urgency.</p>
  </section>

  <section class="value humility">
    <div class="value-icon">
      <svg viewBox="0 0 24 24" fill="#fff"><circle cx="12" cy="6" r="3.2"/><path d="M6 21v-6.5C6 11.5 8.5 10 12 10s6 1.5 6 4.5V21z"/></svg>
    </div>
    <h2>Humility</h2>
    <p>We believe in a flat hierarchy, and that every person within the organisation is a floor sweeper. We’re not always right — we don’t have all the answers — and we know it. We’re all humans after all, and we’re not afraid to ask for help. We encourage everyone to Be Yourself, Be Open, Stay Hungry and Humble, Collaborate, Challenge, Decide and Just Do.</p>
  </section>

  <section class="value integrity">
    <div class="value-icon">
      <svg viewBox="0 0 24 24" fill="none" stroke="#fff" stroke-width="1.6"><path d="M12 3v17M7 21h10M4 6h16"/><path d="M6 6l-3 7h6zM18 6l-3 7h6z"/></svg>
    </div>
    <h2>Integrity</h2>
    <p>We demonstrate honesty, fairness, openness and clear boundaries in all our interactions, behaviours and practices within the organisation and with our clients, stakeholders and the wider community. We act in accordance with our values, even when it’s difficult. We adhere to the highest ethical standards as we strive to do what is right and fair for our clients and for each other.</p>
  </section>
</body>
</html>
```